Business Card Design Project

We need a business card design for a new company based in New York called "Kestrel Co's". We do major installations of energy saving devices primarily LED lighting in large facilities. We would like a double sided card with our contact info on one side with our logo (to be designed) and on the other side the services we provide. We would like a heavy weight glossy card using the colors green and white. The final design should communicate environmental soundness and our market is very upscale corporations.
We would like our logo to illustrate LED lighting and we were thinking if we could get a stock picture of the Calloway Spire Tower lit up on July 4th with red, white and blue LED lighting. The alternative would be anything that connotes environmentally proper thinking. It could be either a picture or a design.

```html
<!DOCTYPE html>
<html lang="en">
<head>
<meta charset="utf-8">
<title>Kestrel Co's — Business Card</title>
<link rel="stylesheet" href="https://fonts.googleapis.com/css2?family=Quicksand:wght@400;500;700&display=swap">
<style>
  :root {
    --backdrop: #2b2b2b;
    --card: #f4f4f4;
    --green: #8cc63f;
    --green-deep: #6fb130;
    --band: #92c43d;
    --white: #ffffff;
  }
  * { margin: 0; padding: 0; box-sizing: border-box; }
  html, body {
    width: 1200px; height: 1200px; overflow: hidden;
    background: var(--backdrop);
    font-family: "Quicksand", sans-serif;
  }
  .card {
    position: absolute; left: 178px; width: 840px; height: 460px;
    background: var(--card); overflow: hidden;
  }
  .card--front { top: 94px; }
  .card--back { top: 625px; }

  .brand-mark {
    position: absolute; left: 369px; top: 143px;
    width: 116px; height: 116px; border-radius: 50%;
    background: var(--green);
  }
  .brand-name {
    position: absolute; left: 0; right: 0; top: 280px;
    text-align: center; color: var(--green-deep);
    font-weight: 700; font-size: 72px; line-height: 1;
  }

  .services {
    position: absolute; left: 40px; width: 582px; top: 84px;
    text-align: center; color: var(--green);
    font-weight: 500; font-size: 24px; line-height: 30px; letter-spacing: 1px;
  }
  .contact-band {
    position: absolute; left: 0; top: 259px; width: 840px; height: 158px;
    background: var(--band);
  }
  .contact-name {
    position: absolute; left: 43px; top: 17px;
    color: var(--white); font-weight: 400; font-size: 31px;
  }
  .contact-list {
    position: absolute; left: 81px; top: 67px; list-style: none;
    color: var(--white); font-weight: 500; font-size: 13px; line-height: 27px;
  }
  .corner-disc {
    position: absolute; left: 626px; top: 165px;
    width: 240px; height: 240px; border-radius: 50%;
    background: radial-gradient(circle at 40% 35%, #9ccf4e, var(--green-deep));
  }
  .website {
    position: absolute; left: 16px; top: 425px;
    color: var(--green-deep); font-weight: 500; font-size: 22px; letter-spacing: 1.5px;
  }
</style>
</head>
<body>
  <section class="card card--front">
    <div class="brand-mark"></div>
    <div class="brand-name">Kestrel Co's</div>
  </section>

  <section class="card card--back">
    <p class="services">Install energy saving devices primarily LED lighting for large facilities</p>
    <div class="contact-band">
      <div class="contact-name">Marcus Hale</div>
      <ul class="contact-list">
        <li>555 214 730</li>
        <li>2140 Harbor Lane New York, NY 10012</li>
        <li>hello@kestrelcos.com</li>
      </ul>
    </div>
    <div class="corner-disc"></div>
    <div class="website">www.kestrelcos.com</div>
  </section>
</body>
</html>
```